Vell Tarnmoor - Brochure - Industrial Construction Services

We need a brochure design based on the power point presentation attached. Our business is named Vell Tarnmoor and is an industrial project services business concentrating on Construction Project Management, Technical Services, and Consulting. We want to communicate that "We offer our clients a
unique systematic approach to solving technical challenges." As you can see from our logo designs we like the colors blue and grey. We are after clean, but innovative design overall. We also seem to like design that have darker style backgrounds. We would like this brochure to be a bi-fold 8.5"x 5.5" size when closed if possible. If any files or graphics are needed in original format please request them. Thanks!

Target Market(s)

Large Oil & Gas, Power Generation, and Engineering Companies.

Industry/Entity Type

Engineering

Font styles to use
Serif

Requirements
Must have
• A strong-lasting first impression.

```html
<!DOCTYPE html>
<html lang="en">
<head>
<meta charset="utf-8">
<title>Vell Tarnmoor – Brochure Spreads</title>
<link href="https://fonts.googleapis.com/css2?family=Tinos:wght@400;700&display=swap" rel="stylesheet">
<style>
  :root{
    --navy:#1c2260;
    --navy-deep:#14184a;
    --band:#3557a6;
    --band-light:#5a78bf;
    --ink:#333;
    --ink-soft:#555;
    --paper:#f4f4f4;
    --bg:#e6e6e4;
    --sky:#bfe0ef;
    --charcoal:#303030;
    --grey-box:#e0e0e0;
    --red:#c0272d;
    --teal:#1f6f8b;
    --venn:#7f9cc9;
    --green:#b8e3a6;
    --salmon:#e9a98e;
  }
  *{margin:0;padding:0;box-sizing:border-box}
  html,body{width:1200px;height:1200px;overflow:hidden}
  body{background:var(--bg);font-family:"Tinos",serif;color:var(--ink);position:relative}

  .spread{position:absolute;left:40px;width:1125px;height:420px;display:flex;box-shadow:0 4px 14px rgba(0,0,0,.18)}
  .spread--summary{top:185px}
  .spread--management{top:710px}
  .page{position:relative;width:50%;height:100%;background:var(--paper);overflow:hidden}
  .page--left{background:linear-gradient(90deg,#f6f6f6 80%,#e4e4e4)}
  .page--right{background:linear-gradient(90deg,#dedede,#f6f6f6 12%)}

  .page-header{position:absolute;left:0;top:0;width:100%;height:75px;background:linear-gradient(90deg,var(--navy-deep),var(--navy) 60%)}
  .page-header h2{position:absolute;left:32px;top:24px;color:#fff;font-weight:700;font-size:25px;letter-spacing:.5px}
  .header-stripe{position:absolute;right:0;top:0;width:240px;height:75px;background:#9aa3b8;clip-path:polygon(0 0,8% 0,28% 100%,20% 100%)}
  .header-band{position:absolute;right:0;top:0;width:225px;height:75px;background:linear-gradient(90deg,var(--band),var(--band-light));clip-path:polygon(8% 0,100% 0,100% 100%,27% 100%)}
  .brand{position:absolute;right:18px;top:26px;display:flex;align-items:center;gap:8px;color:#e8ecf6}
  .brand-dot{width:26px;height:26px;border-radius:50%;border:2px solid #c8d0e4}
  .brand-name{font-size:12px;text-transform:uppercase;letter-spacing:.3px;line-height:1}
  .brand-sub{font-size:5px;letter-spacing:1px;margin-top:3px}

  .page-number{position:absolute;bottom:14px;font-size:16px;color:#111;border-bottom:3px solid var(--teal);padding:0 3px 1px}
  .page--left .page-number{left:36px}
  .page--right .page-number{right:42px}
  .site{position:absolute;bottom:16px;font-size:8px;letter-spacing:1.5px;color:#444}
  .page--left .site{left:210px}
  .page--right .site{left:218px}

  .body-copy{position:absolute;font-size:10px;line-height:1.42;color:var(--ink-soft)}
  .body-copy p{margin-bottom:8px}
  .body-copy ul{list-style:none;margin:0 0 10px 4px}
  .body-copy li{padding-left:20px;position:relative}
  .body-copy li::before{content:"✔";position:absolute;left:0;color:var(--navy);font-size:10px}
  .lead-name{color:var(--red);font-weight:700}

  .venn{position:absolute;left:30px;top:95px}

  .services-title{position:absolute;left:17px;top:84px;font-size:18px;font-weight:700;letter-spacing:1.5px;color:var(--navy-deep)}
  .svc{position:absolute;padding:6px 9px;font-size:9px;line-height:1.4}
  .svc h3{font-size:12px;letter-spacing:1px;margin-bottom:6px}
  .svc--sky{background:var(--sky)}
  .svc--sky h3{color:var(--red)}
  .svc--dark{background:linear-gradient(180deg,#3a3a3a,var(--charcoal));color:#eee}
  .svc--dark h3{color:#fff}
  .svc--grey{background:var(--grey-box)}
  .svc ul{list-style:none}
  .svc li{padding-left:20px;position:relative}
  .svc li::before{content:"♦";position:absolute;left:2px;color:var(--red);font-size:8px}
  .cols{display:flex;gap:12px}

  .cpm-diagram{position:absolute;left:0;top:0}
  .project-art{position:absolute;left:140px;top:118px;width:60px;height:55px;border-radius:4px;background:linear-gradient(180deg,#d8dde6,#8d96a4)}
  .cpm-caption{position:absolute;left:36px;top:335px;font-size:14px;color:#111}

  .org-client{position:absolute;left:140px;top:101px;font-size:16px;color:#222}
  .org-panel{position:absolute;left:47px;top:132px;width:476px;height:250px;background:linear-gradient(180deg,#1f2770,#151b55);border-radius:3px}
  .org-box{position:absolute;text-align:center;font-weight:700;color:#111;background:linear-gradient(180deg,#e4f1fb,#9fc6e6);border:1px solid #c9dced}
  .org-side{position:absolute;left:392px;width:128px;height:18px;font-size:8px;color:#fff;text-align:center;line-height:18px;background:linear-gradient(180deg,#4b6fbe,#2c4d9a);border:1px solid #8da5d8}
  .org-brand{position:absolute;left:70px;top:150px;display:flex;gap:8px;align-items:center;color:#e8ecf6}
  .org-reps{position:absolute;left:68px;top:197px;color:#fff;font-weight:700;font-size:12px;text-decoration:underline}
  .mgr{position:absolute;top:222px;width:52px;height:50px;font-size:8.5px;text-align:center;line-height:1.3;padding-top:5px;background:linear-gradient(180deg,#f2f2f2,#c9c9c9);color:#222}
  .team{position:absolute;top:275px;width:36px;height:42px;font-size:5.5px;text-align:center;line-height:1.35;padding-top:8px;background:linear-gradient(180deg,#bfe0f5,#88b8dc);color:#223}
  .org-base{position:absolute;left:89px;top:332px;width:393px;height:50px;background:var(--green);font-weight:700;font-size:12.5px;color:#1d2a1d}
  .org-base span{position:absolute;text-align:center;line-height:1.3}
</style>
</head>
<body>

<!-- Spread: Summary -->
<section class="spread spread--summary">
  <article class="page page--left">
    <header class="page-header">
      <h2>SUMMARY</h2>
      <div class="header-stripe"></div><div class="header-band"></div>
      <div class="brand"><span class="brand-dot"></span><div><div class="brand-name">Vell Tarnmoor</div><div class="brand-sub">MANAGEMENT &amp; CONSULTING</div></div></div>
    </header>

    <svg class="venn" width="230" height="240" viewBox="0 0 230 240">
      <defs>
        <radialGradient id="vennFill" cx="40%" cy="35%" r="70%">
          <stop offset="0" stop-color="#a9bde0" stop-opacity=".75"/>
          <stop offset="1" stop-color="#6d8cc0" stop-opacity=".75"/>
        </radialGradient>
      </defs>
      <circle cx="112" cy="70" r="58" fill="url(#vennFill)" stroke="#8aa3cf"/>
      <circle cx="62" cy="168" r="58" fill="url(#vennFill)" stroke="#8aa3cf"/>
      <circle cx="162" cy="170" r="58" fill="url(#vennFill)" stroke="#8aa3cf"/>
      <text x="112" y="74" text-anchor="middle" font-family="Tinos,serif" font-size="14" fill="#2a2f4a">I<tspan font-size="11">NTEGRITY</tspan></text>
      <text x="62" y="172" text-anchor="middle" font-family="Tinos,serif" font-size="14" fill="#2a2f4a">K<tspan font-size="11">NOWLEDGE</tspan></text>
      <text x="162" y="174" text-anchor="middle" font-family="Tinos,serif" font-size="14" fill="#2a2f4a">Q<tspan font-size="11">UALITY</tspan></text>
    </svg>

    <div class="body-copy" style="left:260px;top:88px;width:275px">
      <p>Vell Tarnmoor is a highly dynamic Industrial Services organization that specializes in:</p>
      <ul>
        <li>Construction Project Management</li>
        <li>Technical Services</li>
        <li>Consulting</li>
      </ul>
      <p style="margin-bottom:0">We strive to build long-term genuine relationships based on trust and results!</p>
      <p>We proactively seek opportunities to add value by effectively utilizing our knowledge, integrity, and quality attributes to ensure desired results.</p>
      <p>The foundation of our organization’s culture is high integrity, character, and respect. We empower individuals that demonstrate strong leadership skills with the belief that good leaders create more leaders and encourage a strong sense of trust in our organization.</p>
      <p>We look forward to discussing how our partnership will contribute to your success!</p>
    </div>

    <div class="page-number">4</div>
    <div class="site">WWW.VELLTARNMOOR.COM</div>
  </article>

  <article class="page page--right">
    <header class="page-header">
      <h2 style="left:17px">SUMMARY</h2>
      <div class="header-stripe"></div><div class="header-band"></div>
      <div class="brand"><span class="brand-dot"></span><div><div class="brand-name">Vell Tarnmoor</div><div class="brand-sub">MANAGEMENT &amp; CONSULTING</div></div></div>
    </header>

    <h3 class="services-title">Services &amp; Industries</h3>

    <div class="svc svc--sky" style="left:17px;top:108px;width:264px;height:92px">
      <h3>Oil &amp; Gas</h3>
      <ul>
        <li>Upstream (Land &amp; Offshore, Subsea)</li>
        <li>Midstream (Terminals &amp; Plants)</li>
        <li>Downstream (Refineries &amp; LNG)</li>
        <li>Petrochemical</li>
      </ul>
    </div>
    <div class="svc svc--sky" style="left:290px;top:108px;width:265px;height:92px">
      <h3>Technical Services</h3>
      <div class="cols">
        <ul style="width:120px">
          <li>Turnkey Commissioning / Completions</li>
          <li>Instrumentation &amp; Electrical Technicians</li>
          <li>E&amp;I Construction</li>
        </ul>
        <ul style="width:115px">
          <li>Automation Integration Specialists</li>
          <li>Analytical Specialists – Process Analyzers</li>
        </ul>
      </div>
    </div>
    <div class="svc svc--dark" style="left:17px;top:200px;width:264px;height:91px">
      <h3>Power Generation</h3>
      <ul>
        <li>Nuclear Power</li>
        <li>Fossil Fuels</li>
        <li>Renewable Energy</li>
      </ul>
    </div>
    <div class="svc svc--dark" style="left:290px;top:200px;width:265px;height:91px">
      <h3>Consulting</h3>
      <div class="cols">
        <ul style="width:120px">
          <li>Project Management Consulting</li>
          <li>Project Optimization</li>
          <li>Project Controls</li>
        </ul>
        <ul style="width:115px">
          <li>Lean Practices</li>
          <li>Disaster Recovery</li>
          <li>Professional Development</li>
        </ul>
      </div>
    </div>
    <div class="svc svc--sky" style="left:17px;top:291px;width:264px;height:92px">
      <h3>Construction Project Management</h3>
      <div class="cols">
        <ul style="width:118px">
          <li>Complete EPC Oversight</li>
          <li>Owner / Client Representation</li>
          <li>Independent 3rd Party</li>
        </ul>
        <ul style="width:115px">
          <li>Inspection</li>
          <li>Coordination</li>
          <li>All Project Resources</li>
        </ul>
      </div>
    </div>
    <div class="svc svc--grey" style="left:290px;top:291px;width:265px;height:92px;font-size:10px;padding-top:12px">
      <div class="cols">
        <p style="width:118px"><span class="lead-name">Vell Tarnmoor</span> is highly experienced in the Services &amp; Industries displayed.</p>
        <p style="width:122px">We offer complete turn-key solutions and/or simply provide professional resources to augment your current project demands.</p>
      </div>
    </div>

    <div class="page-number">5</div>
    <div class="site">WWW.VELLTARNMOOR.COM</div>
  </article>
</section>

<!-- Spread: Management -->
<section class="spread spread--management">
  <article class="page page--left">
    <header class="page-header">
      <h2>MANAGEMENT</h2>
      <div class="header-stripe"></div><div class="header-band"></div>
      <div class="brand"><span class="brand-dot"></span><div><div class="brand-name">Vell Tarnmoor</div><div class="brand-sub">MANAGEMENT &amp; CONSULTING</div></div></div>
    </header>

    <svg class="cpm-diagram" width="330" height="330" viewBox="0 0 330 330">
      <defs>
        <radialGradient id="projFill" cx="45%" cy="40%" r="65%">
          <stop offset="0" stop-color="#8aa6dc"/><stop offset="1" stop-color="#3b5cae"/>
        </radialGradient>
        <marker id="arrowHead" viewBox="0 0 10 10" refX="6" refY="5" markerWidth="5" markerHeight="5" orient="auto">
          <path d="M0 0 L10 5 L0 10 z" fill="#111"/>
        </marker>
      </defs>
      <ellipse cx="165" cy="178" rx="70" ry="90" fill="url(#projFill)"/>
      <text x="165" y="120" text-anchor="middle" font-family="Tinos,serif" font-size="12" font-weight="700" fill="#1a1f55" text-decoration="underline">PROJECT</text>
      <rect x="92" y="186" width="146" height="16" fill="#7b8794"/>
      <text x="165" y="198" text-anchor="middle" font-family="Tinos,serif" font-size="10" font-weight="700" fill="#111">Contract</text>
      <rect x="50" y="168" width="64" height="56" rx="5" fill="var(--green)" stroke="#8fc07e"/>
      <text x="82" y="199" text-anchor="middle" font-family="Tinos,serif" font-size="11" fill="#222">CLIENT</text>
      <rect x="218" y="168" width="67" height="56" rx="5" fill="var(--salmon)" stroke="#c98a70"/>
      <text x="252" y="188" text-anchor="middle" font-family="Tinos,serif" font-size="8" fill="#222">ENGINEERING</text>
      <text x="252" y="199" text-anchor="middle" font-family="Tinos,serif" font-size="8" fill="#222">&amp;</text>
      <text x="252" y="210" text-anchor="middle" font-family="Tinos,serif" font-size="8" fill="#222">CONSTRUCTION</text>
      <rect x="138" y="255" width="58" height="57" rx="4" fill="#a9c4ea" stroke="#7e9cca"/>
      <circle cx="167" cy="275" r="9" fill="none" stroke="#1a1f55" stroke-width="1.5"/>
      <text x="167" y="299" text-anchor="middle" font-family="Tinos,serif" font-size="7" fill="#1a1f55">Vell Tarnmoor</text>
      <path d="M84 228 C 84 270, 105 285, 132 284" fill="none" stroke="#111" stroke-width="6" marker-end="url(#arrowHead)"/>
      <path d="M202 284 C 235 282, 252 265, 254 232" fill="none" stroke="#111" stroke-width="6" marker-end="url(#arrowHead)"/>
    </svg>
    <div class="project-art" role="img" aria-label="Illustration of an industrial processing plant"></div>
    <div class="cpm-caption">CONSTRUCTION PROJECT MANAGEMENT</div>

    <div class="body-copy" style="left:322px;top:97px;width:212px">
      <p><span class="lead-name">Vell Tarnmoor</span> provides management solutions to clients and has the dynamic ability to manage turn-key project execution or simply provide professionals to augment your project demands.</p>
      <p>We communicate with our clients to ensure the highest level of service possible. Our goal is to establish a mutually beneficial relationship with our clients built on trust and dependability.</p>
      <p>Regardless of the size and scope of your project, we can offer solutions. Our results and high level of client satisfaction are direct indications of the quality of our organization.</p>
    </div>

    <div class="page-number">6</div>
    <div class="site">WWW.VELLTARNMOOR.COM</div>
  </article>

  <article class="page page--right">
    <header class="page-header">
      <h2 style="left:17px">MANAGEMENT</h2>
      <div class="header-stripe"></div><div class="header-band"></div>
      <div class="brand"><span class="brand-dot"></span><div><div class="brand-name">Vell Tarnmoor</div><div class="brand-sub">MANAGEMENT &amp; CONSULTING</div></div></div>
    </header>

    <div class="org-client">CLIENT</div>
    <div class="org-box" style="left:220px;top:83px;width:130px;height:47px;font-size:11px;line-height:47px;letter-spacing:.5px">Project Manager</div>

    <div class="org-panel"></div>
    <svg style="position:absolute;left:0;top:0" width="560" height="420" viewBox="0 0 560 420">
      <g stroke="#c9d6ee" stroke-width="1" fill="none">
        <line x1="286" y1="130" x2="286" y2="143"/>
        <line x1="286" y1="190" x2="286" y2="212"/>
        <line x1="352" y1="166" x2="372" y2="166"/>
        <line x1="372" y1="148" x2="372" y2="201"/>
        <line x1="372" y1="148" x2="392" y2="148"/>
        <line x1="372" y1="175" x2="392" y2="175"/>
        <line x1="372" y1="201" x2="392" y2="201"/>
        <line x1="94" y1="212" x2="478" y2="212"/>
        <line x1="94" y1="212" x2="94" y2="222"/><line x1="149" y1="212" x2="149" y2="222"/>
        <line x1="204" y1="212" x2="204" y2="222"/><line x1="259" y1="212" x2="259" y2="222"/>
        <line x1="314" y1="212" x2="314" y2="222"/><line x1="369" y1="212" x2="369" y2="222"/>
        <line x1="424" y1="212" x2="424" y2="222"/><line x1="478" y1="212" x2="478" y2="222"/>
      </g>
    </svg>

    <div class="org-brand"><span class="brand-dot"></span><div><div class="brand-name" style="font-size:13px">Vell Tarnmoor</div><div class="brand-sub">MANAGEMENT &amp; CONSULTING</div></div></div>
    <div class="org-box" style="left:220px;top:143px;width:132px;height:47px;font-size:11px;padding-top:9px;letter-spacing:.5px">Project Leadership<br><span style="font-weight:400;font-size:7.5px">(one or multiple positions)</span></div>
    <div class="org-side" style="top:139px">Project Controls Lead &amp; Team</div>
    <div class="org-side" style="top:166px">Technical Lead &amp; Team</div>
    <div class="org-side" style="top:192px">Logistics Lead &amp; Team</div>
    <div class="org-reps">CLIENT-REPRESENTATIVES</div>

    <div class="mgr" style="left:68px">Safety<br>Manager</div>
    <div class="mgr" style="left:123px">QA/QC<br>Manager</div>
    <div class="mgr" style="left:178px">Civil/<br>Structural<br>Manager</div>
    <div class="mgr" style="left:233px">Mechanical<br>Manager</div>
    <div class="mgr" style="left:288px">Heavy-Lift<br>Manager</div>
    <div class="mgr" style="left:343px">Piping<br>Manager</div>
    <div class="mgr" style="left:398px">Electrical/<br>Instrument<br>Manager</div>
    <div class="mgr" style="left:453px;font-size:7px">Commissioning<br><span style="font-size:8.5px">Start-up<br>Manager</span></div>

    <div class="team" style="left:76px">Discipline Oversight Team</div>
    <div class="team" style="left:131px">Discipline Oversight Team</div>
    <div class="team" style="left:186px">Discipline Oversight Team</div>
    <div class="team" style="left:241px">Discipline Oversight Team</div>
    <div class="team" style="left:296px">Discipline Oversight Team</div>
    <div class="team" style="left:351px">Discipline Oversight Team</div>
    <div class="team" style="left:406px">Discipline Oversight Team</div>
    <div class="team" style="left:461px">Discipline Oversight Team</div>

    <div class="org-base">
      <span style="left:22px;top:9px">ENGINEERING<br>FIRM</span>
      <span style="right:16px;top:8px">CONSTRUCTION<br>CONTRACTOR</span>
    </div>

    <div class="page-number">7</div>
    <div class="site">WWW.VELLTARNMOOR.COM</div>
  </article>
</section>

</body>
</html>
```